Startup photography business has a new logo, now we need business cards

Design a business card for the two partners of our business.
Our business Brisk Pelican has a new logo and we need to design a business card to showcase it and us.
Our colours of blue and orange are punchy and vivid, but how can we make the most of it on our card?

It should have our name Brisk Pelican
name of partner
phone number
email
website

Industry/Entity Type

Professional Photography

Contact Information for Business Card

Tom Ashworth
+61 400 55 61 72
tom@briskpelican.com.au
briskpelican.com.au

second card
Neil Porter
+61 400 918 263
neil@briskpelican.com.au
briskpelican.com.au

Colors
f37122
f68d4c
33a6d7
0592cd

Requirements
Must have
• one version of our logo, we have included options
• Name
• phone number
• email
• website
Nice to have
• instagram briskpelicanmedia
• twitter briskpelicanmedia
• facebook briskpelicanmedia

```html
<!DOCTYPE html>
<html lang="en">
<head>
<meta charset="utf-8">
<title>Brisk Pelican – Business Card</title>
<link rel="stylesheet" href="https://fonts.googleapis.com/css2?family=Source+Sans+3:ital,wght@0,400;0,600;1,400&display=swap">
<style>
  :root {
    --backdrop: #8c8c8c;
    --card-white: #f2f2f2;
    --brand-blue: #33a6d7;
    --brand-blue-deep: #1ea1d6;
    --brand-orange: #f37122;
    --text-grey: #4d4d4d;
    --white: #ffffff;
  }
  * { box-sizing: border-box; margin: 0; padding: 0; }
  html, body {
    width: 1105px; height: 1200px; overflow: hidden;
    background: var(--backdrop);
    font-family: "Source Sans 3", "Myriad Pro", Arial, sans-serif;
  }
  .canvas { position: relative; width: 1105px; height: 1200px; }
  .card {
    position: absolute; left: 182px; width: 746px; height: 425px;
  }
  .card--front { top: 119px; background: var(--card-white); }
  .card--back { top: 637px; background: var(--brand-blue-deep); }

  .brand-mark {
    position: absolute; display: flex; align-items: center; gap: 14px;
  }
  .card--front .brand-mark { right: 40px; top: 168px; }
  .brand-mark__dot {
    width: 34px; height: 34px; border-radius: 50%;
    border: 5px solid var(--brand-orange);
  }
  .brand-mark__name {
    font-weight: 600; font-size: 34px; letter-spacing: 1px;
    text-transform: uppercase; color: var(--brand-blue); line-height: 1;
  }

  .holder-name {
    position: absolute; left: 39px; top: 252px;
    font-size: 27px; font-weight: 600; letter-spacing: 0.3px;
    text-transform: uppercase; color: var(--brand-blue);
  }
  .divider {
    position: absolute; left: 39px; top: 295px; width: 667px; height: 2px;
    background: var(--brand-orange);
  }
  .contact-list, .social-list {
    position: absolute; list-style: none; top: 309px;
  }
  .contact-list { left: 39px; }
  .social-list { left: 505px; }
  .contact-list li, .social-list li {
    display: flex; align-items: center; gap: 9px;
    height: 28px; font-size: 19px; color: var(--text-grey);
  }
  .contact-icon { width: 18px; height: 18px; flex: none; }
  .social-square {
    width: 19px; height: 19px; flex: none; border-radius: 3px;
    background: var(--text-grey); margin-right: 6px;
  }

  .card--back .brand-mark {
    left: 0; right: 0; top: 150px; justify-content: center; gap: 20px;
  }
  .card--back .brand-mark__dot {
    width: 70px; height: 70px; border: 9px solid var(--card-white);
  }
  .card--back .brand-mark__name { color: var(--card-white); font-size: 52px; }
  .back-url {
    position: absolute; left: 0; right: 0; top: 342px; text-align: center;
    font-style: italic; font-size: 20px; letter-spacing: 2px; color: var(--card-white);
  }
</style>
</head>
<body>
<main class="canvas">
  <section class="card card--front" aria-label="Business card front">
    <div class="brand-mark">
      <span class="brand-mark__dot"></span>
      <span class="brand-mark__name">Brisk Pelican</span>
    </div>
    <h1 class="holder-name">Tom Ashworth</h1>
    <div class="divider"></div>
    <ul class="contact-list">
      <li>
        <svg class="contact-icon" viewBox="0 0 24 24"><path fill="#33a6d7" d="M6.6 10.8a15.1 15.1 0 0 0 6.6 6.6l2.2-2.2c.3-.3.7-.4 1-.2 1.1.4 2.3.6 3.6.6.6 0 1 .4 1 1V20c0 .6-.4 1-1 1A17 17 0 0 1 3 4c0-.6.4-1 1-1h3.5c.6 0 1 .4 1 1 0 1.3.2 2.5.6 3.6.1.3 0 .7-.2 1z"/></svg>
        +61 400 55 61 72
      </li>
      <li>
        <svg class="contact-icon" viewBox="0 0 24 24"><rect x="2" y="5" width="20" height="14" rx="1" fill="#33a6d7"/><path d="M3 6l9 7 9-7" fill="none" stroke="#f2f2f2" stroke-width="1.6"/></svg>
        tom@briskpelican.com.au
      </li>
      <li>
        <svg class="contact-icon" viewBox="0 0 24 24"><circle cx="12" cy="12" r="10" fill="#33a6d7"/><path d="M2 12h20M12 2c3 3 3 17 0 20M12 2c-3 3-3 17 0 20" fill="none" stroke="#f2f2f2" stroke-width="1.4"/></svg>
        briskpelican.com.au
      </li>
    </ul>
    <ul class="social-list">
      <li><span class="social-square"></span>briskpelicanmedia</li>
      <li><span class="social-square"></span>@briskpelicanmedia</li>
      <li><span class="social-square"></span>briskpelicanmedia</li>
    </ul>
  </section>

  <section class="card card--back" aria-label="Business card back">
    <div class="brand-mark">
      <span class="brand-mark__dot"></span>
      <span class="brand-mark__name">Brisk Pelican</span>
    </div>
    <p class="back-url">www.briskpelican.com.au</p>
  </section>
</main>
</body>
</html>
```